We need business cards for our Kashmiri Indian Takeaway Shop. our business sells authentic Kashmiri Cuisine. We also offer catering services and have a BYO Function Room available for private bookings. We would like to see simple but stylish designs that feature Moroccan or Arabic style patterns/ borders and use golds, deep reds, pearl/cream and a touch of black or white. We do not want pictures of curries or Indian spices, chillies etc. The final design should communicate sumptuous, exotic dining.

Target Market(s)

Indian food lovers

Industry/Entity Type

Catering

Contact Information for Business Card

Rahim's Kitchen Authentic Kashmiri Indian Cuisine

Colors
ec2027
fce8d3
fcca95
faa54b

Requirements
Must have
• Simple but stylish design, using Moroccan/Arabic inspired borders or features
Should not have
• Pictures of curries, spices, food etc

```html
<!DOCTYPE html>
<html lang="en">
<head>
<meta charset="utf-8">
<title>Rahim's Kitchen – Business Card</title>
<link rel="stylesheet" href="https://fonts.googleapis.com/css2?family=Arimo:wght@400&display=swap">
<style>
  :root {
    --page-bg: #f0f0f0;
    --brand-red: #ec2027;
    --brand-orange: #faa54b;
    --brand-cream: #fce8d3;
    --ink: #231f20;
  }
  * { margin: 0; padding: 0; box-sizing: border-box; }
  html, body {
    width: 846px;
    height: 1200px;
    overflow: hidden;
    background: var(--page-bg);
    font-family: "Arimo", Arial, sans-serif;
  }
  .canvas {
    position: relative;
    width: 846px;
    height: 1200px;
  }
  .business-card {
    position: absolute;
    left: 223px;
    top: 250px;
    width: 400px;
    height: 700px;
    display: flex;
    flex-direction: column;
  }
  .card-brand {
    position: relative;
    height: 403px;
    background: var(--brand-red);
    color: var(--brand-cream);
    text-align: center;
  }
  .ornament {
    position: absolute;
    left: 120px;
    width: 160px;
    height: 50px;
    background: var(--brand-cream);
    opacity: 0.85;
    border-radius: 25px;
  }
  .ornament--top { top: 87px; }
  .ornament--bottom { top: 244px; }
  .brand-name {
    position: absolute;
    left: 0;
    right: 0;
    top: 156px;
    font-size: 38px;
    font-weight: 400;
    letter-spacing: 1px;
    line-height: 1;
  }
  .brand-tagline {
    position: absolute;
    left: 0;
    right: 0;
    top: 205px;
    font-size: 18px;
    line-height: 1;
  }
  .card-contact {
    position: relative;
    flex: 1;
    background: var(--brand-orange);
    color: var(--ink);
    text-align: center;
  }
  .owner-name {
    position: absolute;
    left: 0;
    right: 0;
    top: 92px;
    font-size: 25px;
    font-weight: 400;
    line-height: 1;
  }
  .owner-role {
    position: absolute;
    left: 0;
    right: 0;
    top: 132px;
    font-size: 14px;
    line-height: 1;
  }
  .services {
    position: absolute;
    left: 0;
    right: 0;
    top: 205px;
    font-size: 15px;
    line-height: 20.5px;
    font-style: normal;
  }
</style>
</head>
<body>
  <main class="canvas">
    <article class="business-card">
      <section class="card-brand">
        <div class="ornament ornament--top" role="img" aria-label="Cream Arabic-style scrollwork flourish above the name"></div>
        <h1 class="brand-name">Rahim's Kitchen</h1>
        <p class="brand-tagline">Authentic Kashmiri Indian Cuisine</p>
        <div class="ornament ornament--bottom" role="img" aria-label="Cream Arabic-style scrollwork flourish below the tagline"></div>
      </section>
      <section class="card-contact">
        <h2 class="owner-name">Rahim Qadir</h2>
        <p class="owner-role">Owner &amp; Chef</p>
        <address class="services">
          Takeaway Shop &amp; Catering,<br>
          BYO Function Room - bookings essential<br>
          14 Maple Lane, Ridgeview Qld, 07- 5550 1842
        </address>
      </section>
    </article>
  </main>
</body>
</html>
```